Business Card Design for Photographer

Updating business card design. Must use included logo. We're a luxury wedding photography business. Elegancy, luxury, consistency are messages we wish to convey.

Visit our website at www.colbyvarnway.com to familiarize yourself more with our brand design currently (fonts, colors etc.). This is what we want to maintain.

Target Market(s)

Luxury Brides and Grooms

Industry/Entity Type

Wedding

Contact Information for Business Card

Current logo (attached to brief)
Name: Colby Varnway
Phone: 5208813047
website/blog
Email

Requirements
Must have
• Current logo (attached to brief)
• Name: Colby Varnway
• Phone: 5208813047
• website/blog
• Email
• Instagram username
Should not have
• bright colors, fonts that don't suit our brand (visit www.colbyvarnway.com)

```html
<!DOCTYPE html>
<html lang="en">
<head>
<meta charset="utf-8">
<title>Colby Varnway Photographers – Business Cards</title>
<link rel="stylesheet" href="https://fonts.googleapis.com/css2?family=Didact+Gothic&family=Open+Sans:wght@400;600&display=swap">
<style>
  :root {
    --canvas-bg: #ecebe8;
    --card-black: #000000;
    --card-light: #e4e4e3;
    --ink-light: #ffffff;
    --ink-dark: #1a1a1a;
    --ink-muted: #7a7a7a;
    --mark-faint: #f3f3f2;
    --photo-wood: #5b5650;
    --photo-wood-dark: #3d3935;
    --photo-bloom: #d9a89a;
    --photo-leaf: #9aa9a3;
  }
  * { margin: 0; padding: 0; box-sizing: border-box; }
  html, body { width: 1200px; height: 1200px; overflow: hidden; }
  body { background: var(--canvas-bg); position: relative; font-family: "Didact Gothic", sans-serif; }

  .card {
    position: absolute;
    left: 200px;
    width: 800px;
    height: 457px;
    box-shadow: 0 6px 18px rgba(0,0,0,0.18);
    overflow: hidden;
  }

  /* Front */
  .card--front { top: 110px; background: var(--card-black); }
  .brand {
    position: absolute;
    left: 0; right: 0; top: 190px;
    display: flex; align-items: center; justify-content: center; gap: 18px;
  }
  .brand__square { width: 44px; height: 44px; background: var(--ink-light); }
  .brand__name {
    color: var(--ink-light);
    font-family: "Didact Gothic", sans-serif;
    font-size: 26px;
    letter-spacing: 4px;
    text-transform: uppercase;
  }

  /* Back */
  .card--back { top: 633px; background: var(--card-light); display: flex; }
  .card__photo {
    width: 408px; height: 100%;
    background:
      radial-gradient(ellipse 170px 130px at 52% 40%, var(--photo-bloom) 0%, var(--photo-leaf) 55%, transparent 80%),
      linear-gradient(180deg, var(--photo-wood) 0%, var(--photo-wood-dark) 100%);
  }
  .card__details { position: relative; flex: 1; }
  .card__mark {
    position: absolute; left: 60px; top: 30px;
    width: 150px; height: 150px;
    background: var(--mark-faint);
  }
  .person { position: absolute; left: 64px; top: 218px; }
  .person__name { font-size: 26px; color: var(--ink-dark); }
  .person__role { font-size: 15px; color: var(--ink-muted); margin-top: 2px; }
  .contact {
    position: absolute; left: 64px; top: 300px;
    list-style: none;
    font-family: "Open Sans", sans-serif;
    font-weight: 600;
    font-size: 17px;
    color: var(--ink-dark);
  }
  .contact__item { display: flex; align-items: center; gap: 12px; height: 27px; }
  .contact__icon { width: 14px; height: 14px; flex: none; }
</style>
</head>
<body>

  <section class="card card--front">
    <div class="brand">
      <span class="brand__square"></span>
      <span class="brand__name">Colby Varnway Photographers</span>
    </div>
  </section>

  <section class="card card--back">
    <div class="card__photo" role="img" aria-label="Photograph of a bridal bouquet of peach and white roses on a weathered wooden bench"></div>
    <div class="card__details">
      <div class="card__mark"></div>
      <div class="person">
        <p class="person__name">Colby Varnway</p>
        <p class="person__role">photographer</p>
      </div>
      <ul class="contact">
        <li class="contact__item">
          <svg class="contact__icon" viewBox="0 0 14 14"><path d="M3 1 L5 1 L6 4 L4.5 5 Q5.5 8 9 9.5 L10 8 L13 9 L13 11 Q12 13 10 13 Q2 11 1 3 Q1 1 3 1 Z" fill="#555"/></svg>
          <span>5208813047</span>
        </li>
        <li class="contact__item">
          <svg class="contact__icon" viewBox="0 0 14 14"><rect x="1" y="3" width="12" height="8" fill="none" stroke="#555" stroke-width="1.2"/><path d="M1 3 L7 8 L13 3" fill="none" stroke="#555" stroke-width="1.2"/></svg>
          <span>colby@colbyvarnway.com</span>
        </li>
        <li class="contact__item">
          <svg class="contact__icon" viewBox="0 0 14 14"><circle cx="7" cy="7" r="5.5" fill="none" stroke="#555" stroke-width="1.2"/><ellipse cx="7" cy="7" rx="2.3" ry="5.5" fill="none" stroke="#555" stroke-width="1"/><line x1="1.5" y1="7" x2="12.5" y2="7" stroke="#555" stroke-width="1"/></svg>
          <span>www.colbyvarnway.com</span>
        </li>
        <li class="contact__item">
          <svg class="contact__icon" viewBox="0 0 14 14"><rect x="1.5" y="1.5" width="11" height="11" fill="none" stroke="#555" stroke-width="1.3"/></svg>
          <span>colbyvarnwayphoto</span>
        </li>
      </ul>
    </div>
  </section>

</body>
</html>
```